Tarrow Consulting WA Business Card

Create an interesting, eye catching and colourful two sided business card. We are a business consulting operation assisting SME's improve all areas of their business. We provide consulting services to assist SME's to create a culture of continuous improvement, making a positive difference in the business. Our tag line is Small changes, big rewards. We want to create a well recognised, innovative brand that can be continued throughout our website, social media and email correspondence.

Target Market(s)

Small to Medium Enterprise Business Owners

Industry/Entity Type

Business Consultant

Contact Information for Business Card

Name of Business: Tarrow Consulting - Small Changes Big Rewards
Dean Fordyce Ph 0407358114 Moira Fordyce Ph 0407935281
Email tarrowconsultingwa@mailbox-example.com
Web address TBA
FaceBook page TBA

BACKSIDE OF CARD

Providing assistance with:

• Organisation & Efficiency
• Revenue generation & Marketing
• Financial Management
• Production quality & delivery
• Systems & Process documentation
• Exit Strategy

Font styles to use
Other font styles liked:
• Calibri

Colors

Designer to choose colors to be used in the design.

Requirements
Must have
• Calibri font

```html
<!DOCTYPE html>
<html lang="en">
<head>
<meta charset="utf-8">
<title>Tarrow Consulting WA – Business Card</title>
<link rel="stylesheet" href="https://fonts.googleapis.com/css2?family=Oswald:wght@400;500&family=Carlito:wght@400;700&display=swap">
<style>
  :root {
    --stage: #1a1a1a;
    --card-light: #f3f3f3;
    --ink: #222222;
    --accent-red: #e4322b;
    --accent-blue: #2a8fc8;
    --blue-deep: #1784bf;
    --blue-glow: #62b6dc;
    --white: #ffffff;
    --brand-square: #2a8fc8;
  }
  * { margin: 0; padding: 0; box-sizing: border-box; }
  html, body { width: 1200px; height: 900px; overflow: hidden; background: var(--stage); }
  .stage { position: relative; width: 1200px; height: 900px; }

  .card {
    position: absolute; top: 200px; width: 309px; height: 502px;
    box-shadow: 4px 5px 6px rgba(0,0,0,.55);
    font-family: "Carlito", Calibri, sans-serif;
  }
  .card--front {
    left: 253px; background: var(--card-light);
    border-radius: 62px 0 62px 0;
  }
  .card--back {
    left: 627px;
    border-radius: 0 62px 0 62px;
    background: radial-gradient(ellipse 65% 55% at 50% 45%, var(--blue-glow) 0%, var(--accent-blue) 60%, var(--blue-deep) 100%);
    color: var(--white);
  }

  .brand-mark {
    position: absolute; left: 50%; transform: translateX(-50%);
  }
  .card--front .brand-mark { top: 92px; width: 78px; height: 78px; background: var(--brand-square); }
  .card--back .brand-mark { top: 70px; width: 84px; height: 84px; background: var(--white); }

  .brand-name {
    position: absolute; left: 0; width: 100%; text-align: center;
    font-family: "Oswald", sans-serif; font-weight: 500; text-transform: uppercase;
  }
  .card--front .brand-name { top: 212px; font-size: 33px; color: var(--ink); letter-spacing: .2px; }
  .card--back .brand-name { top: 166px; font-size: 17px; color: var(--white); letter-spacing: .5px; }

  .contacts { position: absolute; left: 32px; top: 300px; }
  .person-name {
    font-family: "Oswald", sans-serif; font-weight: 400; font-size: 21px;
    color: var(--accent-red); text-transform: uppercase; line-height: 26px;
  }
  .contact-line {
    display: flex; align-items: center; gap: 5px;
    font-size: 14px; color: var(--ink); line-height: 18px;
  }
  .contact-line svg { width: 11px; height: 11px; flex: none; }
  .person + .person { margin-top: 6px; }
  .general { margin-top: 7px; }

  .tagline {
    position: absolute; top: 226px; left: 0; width: 100%; text-align: center;
    font-family: "Oswald", sans-serif; font-size: 18.5px; text-transform: uppercase;
  }
  .services { position: absolute; left: 25px; top: 292px; }
  .services-title { font-weight: 700; font-size: 14.5px; letter-spacing: 1.3px; text-transform: uppercase; margin-bottom: 12px; }
  .services-list { list-style: none; font-size: 17px; line-height: 21px; }
  .services-list li::before {
    content: ""; display: inline-block; width: 8px; height: 8px; border-radius: 50%;
    background: var(--white); margin: 0 4px 2px 0; vertical-align: middle;
  }
</style>
</head>
<body>
<main class="stage">
  <section class="card card--front">
    <div class="brand-mark" role="img" aria-label="Tarrow Consulting brand square"></div>
    <h1 class="brand-name">Tarrow Consulting</h1>
    <div class="contacts">
      <div class="person">
        <p class="person-name">Dean Fordyce</p>
        <p class="contact-line"><svg viewBox="0 0 12 12"><rect x="2.5" y="0.5" width="7" height="11" rx="1.5" fill="none" stroke="#2a8fc8" stroke-width="1.2"/><rect x="4" y="2" width="4" height="6.5" fill="#2a8fc8"/></svg>0407358114</p>
      </div>
      <div class="person">
        <p class="person-name">Moira Fordyce</p>
        <p class="contact-line"><svg viewBox="0 0 12 12"><rect x="2.5" y="0.5" width="7" height="11" rx="1.5" fill="none" stroke="#2a8fc8" stroke-width="1.2"/><rect x="4" y="2" width="4" height="6.5" fill="#2a8fc8"/></svg>0407935281</p>
      </div>
      <div class="general">
        <p class="contact-line"><svg viewBox="0 0 12 12"><rect x="0.5" y="2" width="11" height="8" fill="#2a8fc8"/><path d="M0.5 2 L6 6.5 L11.5 2" fill="none" stroke="#fff" stroke-width="1"/></svg>tarrowconsultingwa@mailbox-example.com</p>
        <p class="contact-line"><svg viewBox="0 0 12 12"><circle cx="6" cy="6" r="5.5" fill="#2a8fc8"/><path d="M0.5 6h11M6 0.5c-2.5 3-2.5 8 0 11M6 0.5c2.5 3 2.5 8 0 11" fill="none" stroke="#fff" stroke-width=".8"/></svg>www.tarrowconsulting.example</p>
        <p class="contact-line"><svg viewBox="0 0 12 12"><circle cx="6" cy="6" r="5.5" fill="#2a8fc8"/></svg>social.example/tarrowconsulting</p>
      </div>
    </div>
  </section>

  <section class="card card--back">
    <div class="brand-mark" role="img" aria-label="Tarrow Consulting brand square"></div>
    <p class="brand-name">Tarrow Consulting</p>
    <h2 class="tagline">Small Changes Big Rewards</h2>
    <div class="services">
      <p class="services-title">Providing assistance with</p>
      <ul class="services-list">
        <li>Organisation &amp; Efficiency</li>
        <li>Revenue generation &amp; Marketing</li>
        <li>Financial Management</li>
        <li>Production quality &amp; delivery</li>
        <li>Systems &amp; Process documentation</li>
        <li>Exit Strategy</li>
      </ul>
    </div>
  </section>
</main>
</body>
</html>
```